Business cards real estate company

We need a design for a business card. It is a company that specializes in real estate sales. There should be space for a photo of the respective employee as well as the website and telephone number on it. Design should be noble, innovative.

Contact Information for Business Card

Website, Name, Position, Telefonnummer

Requirements
Must have
• Photo, logo

```html
<!DOCTYPE html>
<html lang="en">
<head>
<meta charset="utf-8">
<title>Domovia Business Card</title>
<link rel="stylesheet" href="https://fonts.googleapis.com/css2?family=Open+Sans:wght@600;700&display=swap">
<style>
  :root {
    --bg-dark: #262626;
    --bg-mid: #3c3d3d;
    --bg-light: #5b5c5c;
    --brand-green: #a9d65a;
    --frame-lime: #d2e87a;
    --stripe-lime: #c6df45;
    --band-green: #8cc95a;
    --icon-cream: #f3ecb0;
    --text-white: #ffffff;
  }
  * { margin: 0; padding: 0; box-sizing: border-box; }
  html, body { width: 1200px; height: 671px; overflow: hidden; background: var(--bg-dark); }
  .card {
    position: relative;
    width: 1200px;
    height: 671px;
    overflow: hidden;
    font-family: "Open Sans", sans-serif;
    color: var(--text-white);
  }
  .card-backdrop {
    position: absolute; inset: 0;
    background: linear-gradient(100deg, var(--bg-dark) 0%, var(--bg-mid) 50%, var(--bg-light) 100%);
  }
  .brand-name {
    position: absolute;
    left: 96px; top: 62px;
    font-size: 118px;
    font-weight: 600;
    letter-spacing: -1px;
    color: var(--brand-green);
    line-height: 1;
  }
  .photo-frame {
    position: absolute;
    left: 908px; top: 16px;
    width: 240px; height: 288px;
    border: 6px solid var(--frame-lime);
    border-radius: 32px;
  }
  .person {
    position: absolute;
    left: 53px; top: 258px;
    font-weight: 700;
    font-size: 21px;
    letter-spacing: 5px;
    line-height: 34px;
    text-transform: uppercase;
  }
  .divider {
    position: absolute;
    left: 53px; top: 333px;
    width: 1097px; height: 6px;
    background: var(--text-white);
  }
  .contact-row {
    position: absolute;
    left: 53px;
    display: flex;
    align-items: center;
    gap: 27px;
    font-weight: 700;
    font-size: 25px;
    letter-spacing: 0.5px;
  }
  .contact-row.phone { top: 380px; }
  .contact-row.email { top: 451px; }
  .contact-row.web { top: 504px; }
  .contact-row.address {
    left: 628px; top: 381px;
    align-items: flex-start;
    font-size: 18px;
    line-height: 33px;
    letter-spacing: 0;
    gap: 35px;
  }
  .icon-box {
    width: 40px; height: 40px;
    border: 3px solid var(--icon-cream);
    border-radius: 5px;
    display: flex; align-items: center; justify-content: center;
    flex-shrink: 0;
  }
  .icon-box svg { width: 26px; height: 26px; }
  .bottom-bands { position: absolute; left: 0; top: 0; }
</style>
</head>
<body>
<div class="card">
  <div class="card-backdrop" role="img" aria-label="Soft-focus photo of a bright modern office interior"></div>

  <div class="brand-name">Domovia</div>

  <div class="photo-frame" role="img" aria-label="Space for the employee's portrait photo"></div>

  <div class="person">
    <p class="person-name">Your Name Here</p>
    <p class="person-role">Owner</p>
  </div>

  <div class="divider"></div>

  <div class="contact-row phone">
    <span class="icon-box">
      <svg viewBox="0 0 24 24" fill="none" stroke="#f3ecb0" stroke-width="2"><rect x="7" y="2" width="10" height="20" rx="2"/><line x1="7" y1="18" x2="17" y2="18"/><line x1="7" y1="5" x2="17" y2="5"/></svg>
    </span>
    <span>01555 204 318</span>
  </div>

  <div class="contact-row email">
    <span class="icon-box">
      <svg viewBox="0 0 24 24" fill="#f3ecb0"><path d="M2 20 L22 20 L18 16 L6 16 Z"/><path d="M11 3 L11 15 L4 15 Z"/><path d="M13 6 L13 15 L19 15 Z"/></svg>
    </span>
    <span>YOUR MAIL@DOMOVIA.COM</span>
  </div>

  <div class="contact-row web">
    <span class="icon-box">
      <svg viewBox="0 0 24 24"><circle cx="12" cy="12" r="10" fill="#f3ecb0"/><path d="M7 7 C10 6 11 9 9 11 C7 13 10 15 8 18 M14 5 C16 8 13 9 15 12 C17 14 15 17 17 18" stroke="#3c3d3d" stroke-width="2" fill="none"/></svg>
    </span>
    <span>WWW.DOMOVIA.COM</span>
  </div>

  <div class="contact-row address">
    <span class="icon-box">
      <svg viewBox="0 0 24 24"><path d="M12 2 C7.6 2 5 5.2 5 9 C5 14 12 22 12 22 C12 22 19 14 19 9 C19 5.2 16.4 2 12 2 Z" fill="#f3ecb0"/><circle cx="12" cy="9" r="3" fill="#3c3d3d"/></svg>
    </span>
    <span class="address-text">Lakeview Plaza (2nd Floor),<br>Riverside, Northport-4410</span>
  </div>

  <svg class="bottom-bands" width="1200" height="671" viewBox="0 0 1200 671">
    <path d="M0 589 H610 C640 589 650 596 636 612 L630 618 H0 Z" fill="var(--stripe-lime)"/>
    <path d="M618 671 C650 630 672 597 730 594 H1200 V671 Z" fill="var(--band-green)"/>
  </svg>
</div>
</body>
</html>
```